Retail Jewelry Business Card Design Project

We are in need of a new business card design for a retail jewelry store. This store is in the business of fine jewelry including but not specific to bridal jewelry, diamonds, designer jewelry and watches.

This store has been in business for 20 years but continues to strive for a modern professional appeal. The main colors use for this business are a royal blue, white and silver.

Target Market(s)

Target market is ages 18-50

Industry/Entity Type

Jewelry

Requirements
Must have
• Sales Person Name
Sales Person Email Address

Store Address
Store Phone
Website

Standard business card size. No odd shapes or sizes.
Nice to have
• Overall modern feel for card.

We have thought that a design with a nice feature of the logo on the back of the card would be nice but open to ideas.
Should not have
• No specific images of jewelry should be used.

```html
<!DOCTYPE html>
<html lang="en">
<head>
<meta charset="utf-8">
<title>Marlow Hayes Fine Jewelry — Business Card</title>
<link rel="stylesheet" href="https://fonts.googleapis.com/css2?family=Poppins:wght@600&display=swap">
<style>
  :root {
    --royal: #3a35a8;
    --royal-deep: #2b2790;
    --royal-light: #4c48c0;
    --silver: #c9ccd3;
    --silver-light: #f1f2f5;
    --silver-dark: #9a9ea8;
    --white: #ffffff;
    --stage: #e7e9ee;
    --ink-blue: #3a35a8;
  }
  * { box-sizing: border-box; margin: 0; padding: 0; }
  html, body { width: 1200px; height: 788px; overflow: hidden; }
  body {
    background: var(--stage);
    font-family: "Poppins", Arial, sans-serif;
    font-weight: 600;
    position: relative;
  }
  .card {
    position: absolute;
    top: 245px;
    width: 520px;
    height: 297px;
    border-radius: 4px;
    overflow: hidden;
    box-shadow: 0 6px 18px rgba(0,0,0,0.18);
  }
  .card--front { left: 50px; background: linear-gradient(160deg, var(--royal-light), var(--royal) 55%, var(--royal-deep)); }
  .card--back { left: 630px; background: linear-gradient(180deg, var(--white), var(--silver-light) 60%, #e2e4e9); }

  .silver-band {
    position: absolute; left: 0; width: 100%; height: 9px;
    background: linear-gradient(180deg, var(--silver-dark), var(--silver-light) 45%, var(--silver) 100%);
  }
  .card--front .silver-band--top { top: 14px; }
  .card--front .silver-band--bottom { bottom: 14px; }

  .logo-plate {
    position: absolute; left: 100px; top: 62px;
    width: 246px; height: 120px;
    background: var(--white);
    border-radius: 18px;
    display: flex; flex-direction: column; align-items: center; justify-content: center;
  }
  .brand-name {
    color: var(--ink-blue);
    text-align: center;
    line-height: 1.15;
    font-size: 26px;
  }
  .brand-name .brand-sub { display: block; font-size: 15px; letter-spacing: 2px; }

  .card--back .brand-name { position: absolute; top: 18px; left: 0; width: 100%; font-size: 24px; }
  .card--back .brand-name .brand-sub { font-size: 13px; }

  .contact-band {
    position: absolute; left: 0; top: 96px; width: 100%; height: 96px;
    background: linear-gradient(180deg, var(--royal-light), var(--royal) 60%, var(--royal-deep));
  }
  .contact-band::before, .contact-band::after {
    content: ""; position: absolute; left: 0; width: 100%; height: 6px;
    background: linear-gradient(180deg, var(--silver-dark), var(--silver-light), var(--silver));
  }
  .contact-band::before { top: -6px; }
  .contact-band::after { bottom: -6px; }

  .contact-item { position: absolute; display: flex; align-items: center; gap: 9px; color: var(--white); font-size: 11.5px; line-height: 1.35; }
  .contact-item--address { left: 22px; top: 14px; }
  .contact-item--phone { right: 24px; top: 16px; font-size: 13px; }
  .contact-item--web { left: 150px; top: 60px; font-size: 13px; }

  .icon { width: 20px; height: 20px; flex: none; }

  .person { position: absolute; top: 212px; left: 0; width: 100%; text-align: center; color: var(--ink-blue); }
  .person-name { font-size: 14px; }
  .person-email { display: flex; justify-content: center; align-items: center; gap: 10px; margin-top: 8px; font-size: 16px; }
  .person-email .icon { width: 24px; height: 24px; }
</style>
</head>
<body>

  <section class="card card--front" aria-label="Card front">
    <div class="silver-band silver-band--top"></div>
    <div class="logo-plate">
      <div class="brand-name">Marlow Hayes<span class="brand-sub">FINE JEWELRY</span></div>
    </div>
    <div class="silver-band silver-band--bottom"></div>
  </section>

  <section class="card card--back" aria-label="Card back">
    <div class="brand-name">Marlow Hayes<span class="brand-sub">FINE JEWELRY</span></div>

    <div class="contact-band">
      <div class="contact-item contact-item--address">
        <svg class="icon" viewBox="0 0 20 20" aria-hidden="true">
          <circle cx="10" cy="10" r="9.5" fill="#1d4f9c" stroke="#c9ccd3"/>
          <path d="M5 10.5 L10 6 L15 10.5 M6.8 9.5 V14 H13.2 V9.5" fill="none" stroke="#fff" stroke-width="1.4"/>
        </svg>
        <span>2280 Linden Avenue<br>Bay Harbor, FL 32550</span>
      </div>
      <div class="contact-item contact-item--phone">
        <svg class="icon" viewBox="0 0 20 20" aria-hidden="true">
          <circle cx="10" cy="10" r="9.5" fill="#2f86c9" stroke="#c9ccd3"/>
          <path d="M7 5.5 L8.6 7.8 L7.7 9 Q9 11.5 11 12.3 L12.2 11.4 L14.5 13 L13.5 14.5 Q9 14.5 5.6 8 Z" fill="#fff"/>
        </svg>
        <span>(555)214-0386</span>
      </div>
      <div class="contact-item contact-item--web">
        <svg class="icon" viewBox="0 0 20 20" aria-hidden="true">
          <circle cx="10" cy="10" r="8" fill="#2f86c9"/>
        </svg>
        <span>www.marlowhayesjewelry.com</span>
      </div>
    </div>

    <div class="person">
      <div class="person-name">Marlow Hayes Ellison</div>
      <div class="person-email">
        <svg class="icon" viewBox="0 0 24 24" aria-hidden="true">
          <rect x="3" y="7" width="18" height="12" rx="1.5" fill="#2f86c9"/>
          <path d="M3.5 8 L12 14 L20.5 8" fill="none" stroke="#fff" stroke-width="1.4"/>
        </svg>
        <span>marlow@marlowhayesjewelry.com</span>
      </div>
    </div>
  </section>

</body>
</html>
```